Long term design collaboration - mobile app design & web app design

We are looking for a talented mobile designer to help us improve our UI & UX for mobile app and web app.

The screens that need to be redesigned are attached.

There is potentially a lot more work in future design available for the successful candidate.
The successful candidate would have to take part in daily stand-up around 3 times per week.
The successful candidate would join a dev team
We are software company that does property management

```html
<!DOCTYPE html>
<html lang="en">
<head>
<meta charset="utf-8">
<title>Larkhill dashboard – design board</title>
<link href="https://fonts.googleapis.com/css2?family=DM+Sans:wght@400;500;600;700&display=swap" rel="stylesheet">
<style>
:root{
  --board:#d1daea;
  --band:#dbe2ef;
  --white:#ffffff;
  --page:#f4f4f5;
  --ink:#1d1f23;
  --muted:#6c7078;
  --line:#e3e5ea;
  --blue:#2953b6;
  --blue-soft:#e8eefb;
  --warn-bg:#fdf4e2;
  --warn-line:#f2c46c;
  --orange:#f2a33a;
  --red:#e5484d;
  --green:#1f9d62;
  --green-soft:#e4f5eb;
}
*{box-sizing:border-box;margin:0;padding:0}
html,body{width:1200px;height:981px;overflow:hidden;background:var(--white)}
body{font-family:"DM Sans",Arial,sans-serif;color:var(--ink)}
.board{position:absolute;left:0;top:0;width:2124px;height:1736px;transform:scale(.56497);transform-origin:0 0}
.file-tag{position:absolute;left:20px;top:3px;padding:2px 4px;background:#e7ebf3;font-size:5px;color:var(--muted)}
.canvas{position:absolute;left:20px;top:20px;width:2084px;height:1696px;background:var(--board)}
.section-band{position:absolute;height:36px;background:var(--band);padding-left:7px;font-size:17px;font-weight:600;line-height:36px}
svg.icon{display:inline-block;fill:none;stroke:currentColor;stroke-width:1.6;stroke-linecap:round;stroke-linejoin:round;flex:none}

/* ---------- web app ---------- */
.app{position:absolute;width:941px;height:529px;background:var(--page);overflow:hidden}
.topbar{position:absolute;left:0;top:0;width:100%;height:43px;background:var(--white);border-bottom:1px solid var(--line)}
.topbar .menu{position:absolute;left:19px;top:15px;width:13px;height:13px;color:#5b5f66}
.brand{position:absolute;left:46px;top:13px;font-size:14px;font-weight:700;color:var(--blue);line-height:16px}
.search{position:absolute;left:205px;top:8px;width:325px;height:27px;border:1px solid #d7dae0;border-radius:5px;display:flex;align-items:center;gap:6px;padding-left:10px;font-size:7.5px;color:var(--muted)}
.search .icon{width:10px;height:10px}
.bell{position:absolute;left:792px;top:12px;width:18px;height:18px;border-radius:50%;background:#f1f2f4;display:flex;align-items:center;justify-content:center;color:var(--ink)}
.bell .icon{width:10px;height:10px}
.bell .dot{position:absolute;right:-3px;top:-3px;width:7px;height:7px;border-radius:50%;background:var(--red);color:#fff;font-size:4.5px;line-height:7px;text-align:center}
.avatar{position:absolute;left:828px;top:9px;width:24px;height:24px;border-radius:50%;background:linear-gradient(135deg,#8f7b6c,#3e4a58)}
.avatar::after{content:"";position:absolute;right:-1px;bottom:0;width:6px;height:6px;border-radius:50%;background:#22b36a;border:1px solid #fff}
.user{position:absolute;left:858px;top:9px;line-height:12px}
.user b{display:block;font-size:8.5px;font-weight:600}
.user span{font-size:7.5px;color:var(--muted)}
.user-caret{position:absolute;left:913px;top:19px;width:0;height:0;border-left:3.5px solid transparent;border-right:3.5px solid transparent;border-top:4px solid #555}

.sidebar{position:absolute;left:0;top:43px;width:169px;bottom:0;background:var(--white);padding-top:18px}
.sidebar::after{content:"";position:absolute;right:0;top:18px;width:3px;height:23px;background:var(--blue);border-radius:2px}
.nav-item{height:23.7px;margin:0 14px 0 12px;padding-left:8px;display:flex;align-items:center;gap:7px;font-size:7.5px;color:#52565d;border-radius:7px}
.nav-item .icon{width:10px;height:10px}
.nav-item.active{background:var(--blue-soft);color:var(--blue);font-weight:600}
.app.collapsed .sidebar{width:37px}
.app.collapsed .nav-item{margin:0 6px;padding-left:7px;width:23px}
.app.collapsed .nav-item span{display:none}

.main{position:absolute;left:169px;top:43px;right:0;bottom:0}
.app.collapsed .main{left:37px}
.main > *{position:absolute;left:24px;right:25px}
.app.collapsed .main > *{left:25px;right:16px}
.page-title{top:19px;font-size:17px;font-weight:500;line-height:20px;display:flex;align-items:center;gap:10px}
.page-title .icon{width:11px;height:11px}
.page-sub{top:43px;font-size:7.3px;color:var(--muted);line-height:10px}
.main > .btn-report,
.app.collapsed .main > .btn-report{left:auto;top:22px;width:98px;height:27px;background:var(--blue);color:#fff;border-radius:4px;font-size:7.5px;font-weight:600;display:flex;align-items:center;justify-content:center}
.main > .btn-report{right:25px}
.app.collapsed .main > .btn-report{right:16px}

.setup{top:66px;height:36px;background:var(--warn-bg);border:1px solid var(--warn-line);border-radius:4px;padding:0 14px 0 36px}
.progress{position:absolute;left:5px;top:6px;width:23px;height:23px;border-radius:50%;border:2.5px solid var(--orange);border-left-color:#f7dcb0;background:#fff;font-size:7px;font-weight:700;display:flex;align-items:center;justify-content:center}
.setup h3{font-size:8.5px;font-weight:500;margin-top:6px;line-height:11px}
.steps{display:flex;gap:5px;font-size:7px;color:var(--muted);margin-top:4px;line-height:9px}
.steps li{list-style:none;display:flex;align-items:center;gap:3px}
.steps li::before{content:"";width:3px;height:3px;border-radius:50%;background:var(--orange)}
.steps li.link{color:var(--blue);text-decoration:underline}
.setup .toggle{position:absolute;right:10px;top:15px;width:0;height:0;border-left:3.5px solid transparent;border-right:3.5px solid transparent;border-top:4px solid #333}
.setup .chev{position:absolute;right:8px;top:12px;width:10px;height:10px}

.tabs{height:19px;background:#fff;border:1px solid var(--line);border-radius:4px;display:flex;padding:1px;font-size:7.5px}
.main > .tabs,
.app.collapsed .main > .tabs{top:116px;width:98px;right:auto}
.app.collapsed .main > .tabs{top:124px}
.tab{flex:1;display:flex;align-items:center;justify-content:center;border-radius:3px}
.tab.on{background:var(--blue);color:#fff}

.card{background:var(--white);border:1px solid var(--line);border-radius:6px;padding:0 11px}
.card-head{height:33px;border-bottom:1px solid var(--line);display:flex;align-items:center;justify-content:space-between}
.card-head h4{font-size:11.5px;font-weight:500}
.view{font-size:7.5px;color:var(--blue);display:flex;align-items:center;gap:2px}
.view .icon{width:7px;height:7px}
.rows{padding-top:5px}
.row{height:18.2px;display:flex;align-items:center;justify-content:space-between;font-size:7px}
.row dt{font-weight:500;display:flex;align-items:center;gap:4px}
.row dd{color:#3a3d43}
.info{width:8px;height:8px;color:var(--muted)}
.info.alert{color:var(--red)}
.general{top:157px;height:117px}
.card-grid{top:288px;height:135px;display:grid;grid-template-columns:repeat(4,1fr);gap:13px}
.card-grid .card{height:135px}

.dropdown{position:absolute;left:830px;top:43px;width:90px;height:64px;background:#fff;border-radius:5px;box-shadow:0 2px 8px rgba(30,40,60,.12);padding:6px 8px;font-size:7px;display:flex;flex-direction:column;gap:8px}
.dropdown div{display:flex;align-items:center;gap:5px}
.dropdown .icon{width:8px;height:8px}
.dropdown .logout{color:var(--red)}

.row-card{height:37px;display:flex;align-items:center;justify-content:space-between;background:#fff;border:1px solid var(--line);border-radius:6px;padding:0 14px 0 15px;font-size:11.5px;font-weight:500}
.row-card .icon{width:9px;height:9px}
.row-card .badge{font-size:7px;font-weight:500;color:var(--green);background:var(--green-soft);padding:3px 6px;border-radius:3px;margin-left:8px}
.row-card .label{display:flex;align-items:center}

/* ---------- mobile ---------- */
.phone{position:absolute;width:210px;background:var(--page);overflow:hidden}
.status{position:absolute;left:0;top:0;width:100%;height:22px;background:#fff;font-size:8px;font-weight:600;padding:5px 8px}
.status .bars{position:absolute;right:8px;top:8px;display:flex;gap:3px;align-items:center}
.status .bars i{display:block;background:var(--ink);border-radius:1px}
.phone-head{position:absolute;left:0;top:22px;width:100%;height:24px;background:#fff;display:flex;align-items:center;padding:0 10px;font-size:12px;font-weight:600;gap:6px}
.phone-head .icon{width:10px;height:10px}
.phone-head .greet{flex:1;text-align:center}
.phone-head .alarm{color:var(--red)}
.phone .body{position:absolute;left:10px;right:10px}
.phone .card{padding:0 8px;border-radius:5px}
.phone .card-head{height:28px}
.phone .card-head h4{font-size:10px;font-weight:600}
.phone .rows{padding-top:4px}
.phone .row{font-size:6.8px;height:18.2px}
.phone .row dt{font-weight:500}
.phone .tabs{position:absolute;left:10px;right:10px;height:27px;font-size:7.5px;padding:2px;border-radius:5px}
.phone .setup{position:absolute;height:34px;border-radius:5px;padding-left:38px}
.phone .setup h3{margin-top:11px;font-size:8.2px}
.phone .over-title{font-size:12px;font-weight:600}
.phone .over-sub{font-size:7px;color:var(--muted);line-height:10px;margin-top:4px}
.bottom-nav{position:absolute;left:0;width:100%;height:44px;background:#fff;display:flex;justify-content:space-around;padding:8px 6px 0}
.nav-tab{width:34px;height:24px;border-radius:4px;display:flex;flex-direction:column;align-items:center;gap:2px;padding-top:3px;font-size:5.5px;color:var(--muted)}
.nav-tab .icon{width:9px;height:9px}
.nav-tab.on{background:var(--blue-soft);color:var(--blue);font-weight:600}
.home-bar{position:absolute;left:67px;width:76px;height:3px;border-radius:2px;background:var(--ink)}
.sub-divider{border-top:1px solid var(--line);margin:4px 0 0}
.question{font-size:9px;font-weight:600}
.option{height:25px;background:#fff;border:1px solid var(--line);border-radius:4px;display:flex;align-items:center;gap:6px;padding-left:8px;font-size:7px;font-weight:500;margin-bottom:10px}
.radio{width:9px;height:9px;border-radius:50%;border:1.2px solid var(--ink);display:flex;align-items:center;justify-content:center}
.radio.on{border-color:var(--blue)}
.radio.on::after{content:"";width:5px;height:5px;border-radius:50%;background:var(--blue)}
.actions{position:absolute;left:0;width:100%;background:#fff;padding:8px 10px 0;display:flex;gap:8px;height:56px;border-top:1px solid #eceef2}
.actions div{flex:1;height:24px;border-radius:3px;display:flex;align-items:center;justify-content:center;font-size:7.5px;font-weight:500}
.btn-ghost{border:1px solid var(--blue);color:var(--blue)}
.btn-solid{background:var(--blue);color:#fff}
</style>
</head>
<body>
<svg width="0" height="0" style="position:absolute">
  <defs>
    <symbol id="i-menu" viewBox="0 0 16 16"><path d="M2 4h12M2 8h12M2 12h12"/></symbol>
    <symbol id="i-search" viewBox="0 0 16 16"><circle cx="7" cy="7" r="5"/><path d="M11 11l3 3"/></symbol>
    <symbol id="i-bell" viewBox="0 0 16 16"><path d="M4 11V7a4 4 0 0 1 8 0v4l1 1.5H3z"/><path d="M6.5 14h3"/></symbol>
    <symbol id="i-user" viewBox="0 0 16 16"><circle cx="8" cy="8" r="6.5"/><circle cx="8" cy="6.5" r="2.2"/><path d="M4 12.5c1-2 2.4-2.6 4-2.6s3 .6 4 2.6"/></symbol>
    <symbol id="i-swap" viewBox="0 0 16 16"><path d="M3 5h10l-3-3M13 11H3l3 3"/></symbol>
    <symbol id="i-dollar" viewBox="0 0 16 16"><circle cx="8" cy="8" r="6.5"/><path d="M10 5.8c-.5-.6-1.2-.9-2-.9-1.2 0-2 .6-2 1.5 0 2 4 1 4 3 0 .9-.9 1.6-2 1.6-.9 0-1.6-.3-2.1-.9M8 3.8v8.4"/></symbol>
    <symbol id="i-doc" viewBox="0 0 16 16"><path d="M4 1.5h5.5L12.5 4.5V14.5H4z"/><path d="M6 7h4.5M6 9.5h4.5M6 12h3"/></symbol>
    <symbol id="i-mail" viewBox="0 0 16 16"><rect x="2" y="3.5" width="12" height="9" rx="1"/><path d="M2.5 4.5L8 9l5.5-4.5"/></symbol>
    <symbol id="i-file" viewBox="0 0 16 16"><path d="M4 1.5h5.5L12.5 4.5V14.5H4z"/><path d="M9.5 1.5v3h3"/></symbol>
    <symbol id="i-chev" viewBox="0 0 16 16"><path d="M6 3l5 5-5 5"/></symbol>
    <symbol id="i-down" viewBox="0 0 16 16"><path d="M3 6l5 5 5-5"/></symbol>
    <symbol id="i-info" viewBox="0 0 16 16"><circle cx="8" cy="8" r="6.5"/><path d="M8 7.5v4M8 5h.01"/></symbol>
    <symbol id="i-help" viewBox="0 0 16 16"><circle cx="8" cy="8" r="6.5"/><path d="M6.2 6.2a1.9 1.9 0 1 1 2.6 1.7c-.6.3-.8.7-.8 1.3M8 11.5h.01"/></symbol>
    <symbol id="i-back" viewBox="0 0 16 16"><path d="M13.5 8H2.5M7 3.5L2.5 8 7 12.5"/></symbol>
    <symbol id="i-logout" viewBox="0 0 16 16"><path d="M6 2.5H3v11h3M10 5l3 3-3 3M13 8H6"/></symbol>
    <symbol id="i-home" viewBox="0 0 16 16"><path d="M2.5 7L8 2.5 13.5 7v6.5h-11z" fill="currentColor"/></symbol>
    <symbol id="i-msg" viewBox="0 0 16 16"><path d="M2.5 3h11v8H6l-3.5 2.5z"/></symbol>
  </defs>
</svg>

<div class="board">
  <div class="file-tag">Larkhill dashboard</div>
  <div class="canvas"></div>

  <!-- ===== Page 1 ===== -->
  <div class="section-band" style="left:93px;top:42px;width:941px">Page 1</div>
  <section class="app" style="left:93px;top:93px">
    <header class="topbar">
      <svg class="icon menu"><use href="#i-menu"/></svg>
      <div class="brand">Larkhill</div>
      <div class="search"><svg class="icon"><use href="#i-search"/></svg>Search</div>
      <div class="bell"><svg class="icon"><use href="#i-bell"/></svg><span class="dot">4</span></div>
      <div class="avatar" role="img" aria-label="Profile photo of the signed-in user"></div>
      <div class="user"><b>Dan Fallow</b><span>Account</span></div>
      <div class="user-caret"></div>
    </header>
    <nav class="sidebar">
      <div class="nav-item active"><svg class="icon"><use href="#i-user"/></svg><span>User Directory</span></div>
      <div class="nav-item"><svg class="icon"><use href="#i-swap"/></svg><span>Switch Development</span></div>
      <div class="nav-item"><svg class="icon"><use href="#i-dollar"/></svg><span>Service Change</span></div>
      <div class="nav-item"><svg class="icon"><use href="#i-doc"/></svg><span>Property Balane</span></div>
      <div class="nav-item"><svg class="icon"><use href="#i-mail"/></svg><span>Sending Letter</span></div>
      <div class="nav-item"><svg class="icon"><use href="#i-file"/></svg><span>Regular Services</span></div>
    </nav>
    <main class="main">
      <h1 class="page-title">Overview</h1>
      <p class="page-sub">Lorem ipsum dolor sit amet consectetur. Sem sit pellentesque mauris proin tortor pellentesque.</p>
      <div class="btn-report">Report</div>
      <div class="setup">
        <div class="progress">05</div>
        <h3>Please complete basic Setup</h3>
        <ul class="steps"><li class="link">Service Charge Schedules</li><li>Service Charge Appointment</li><li>Invite residents &amp; leaseholders</li><li>Connect payment provider</li></ul>
        <div class="toggle"></div>
      </div>
      <div class="tabs"><div class="tab on">Summary</div><div class="tab">Details</div></div>
      <div class="card general">
        <div class="card-head"><h4>General</h4><span class="view">View Detail <svg class="icon"><use href="#i-chev"/></svg></span></div>
        <dl class="rows">
          <div class="row"><dt>Units</dt><dd>85</dd></div>
          <div class="row"><dt>Address</dt><dd>42 Larchmere Road, London, N4 2QT</dd></div>
          <div class="row"><dt>Section 20 Limites</dt><dd>12</dd></div>
          <div class="row"><dt>Handover Date</dt><dd>NA</dd></div>
        </dl>
      </div>
      <div class="card-grid">
        <div class="card">
          <div class="card-head"><h4>Compliance</h4><span class="view">View Detail <svg class="icon"><use href="#i-chev"/></svg></span></div>
          <dl class="rows">
            <div class="row"><dt>Asbestos <svg class="icon info"><use href="#i-info"/></svg></dt><dd>NA</dd></div>
            <div class="row"><dt>Legionellas <svg class="icon info alert"><use href="#i-help"/></svg></dt><dd>--</dd></div>
            <div class="row"><dt>Gutter</dt><dd>Overdue 10/12/2023</dd></div>
            <div class="row"><dt>Gutters</dt><dd>NA</dd></div>
            <div class="row"><dt>Dry Risers</dt><dd>NA</dd></div>
          </dl>
        </div>
        <div class="card">
          <div class="card-head"><h4>Insurance</h4><span class="view">View Detail <svg class="icon"><use href="#i-chev"/></svg></span></div>
          <dl class="rows">
            <div class="row"><dt>Terrorism</dt><dd>NA</dd></div>
            <div class="row"><dt>Buildings</dt><dd>NA</dd></div>
            <div class="row"><dt>Engineering</dt><dd>NA</dd></div>
            <div class="row"><dt>D&amp;O</dt><dd>NA</dd></div>
            <div class="row"><dt>Reinstatement</dt><dd>NA</dd></div>
          </dl>
        </div>
        <div class="card">
          <div class="card-head"><h4>Service Charge</h4><span class="view">View Detail <svg class="icon"><use href="#i-chev"/></svg></span></div>
          <dl class="rows">
            <div class="row"><dt>Year End</dt><dd>12/12/2024</dd></div>
            <div class="row"><dt>Demand Dates</dt><dd>NA</dd></div>
          </dl>
        </div>
        <div class="card">
          <div class="card-head"><h4>Cases</h4><span class="view">View Detail <svg class="icon"><use href="#i-chev"/></svg></span></div>
          <dl class="rows">
            <div class="row"><dt>Are we Responsible ? <svg class="icon info"><use href="#i-info"/></svg></dt><dd>No</dd></div>
            <div class="row"><dt>Demand Dates</dt><dd>NA</dd></div>
          </dl>
        </div>
      </div>
    </main>
  </section>

  <!-- ===== Page 1 collapsed ===== -->
  <div class="section-band" style="left:1090px;top:42px;width:941px">Page 1 (Collapsed Menu)</div>
  <section class="app collapsed" style="left:1090px;top:93px">
    <header class="topbar">
      <svg class="icon menu"><use href="#i-menu"/></svg>
      <div class="brand">Larkhill</div>
      <div class="search"><svg class="icon"><use href="#i-search"/></svg>Search</div>
      <div class="bell"><svg class="icon"><use href="#i-bell"/></svg><span class="dot">4</span></div>
      <div class="avatar" role="img" aria-label="Profile photo of the signed-in user"></div>
      <div class="user"><b>Dan Fallow</b><span>Account</span></div>
      <div class="user-caret"></div>
    </header>
    <nav class="sidebar">
      <div class="nav-item active"><svg class="icon"><use href="#i-user"/></svg><span>User Directory</span></div>
      <div class="nav-item"><svg class="icon"><use href="#i-swap"/></svg><span>Switch Development</span></div>
      <div class="nav-item"><svg class="icon"><use href="#i-dollar"/></svg><span>Service Change</span></div>
      <div class="nav-item"><svg class="icon"><use href="#i-doc"/></svg><span>Property Balane</span></div>
      <div class="nav-item"><svg class="icon"><use href="#i-mail"/></svg><span>Sending Letter</span></div>
      <div class="nav-item"><svg class="icon"><use href="#i-file"/></svg><span>Regular Services</span></div>
    </nav>
    <main class="main">
      <h1 class="page-title">Overview</h1>
      <p class="page-sub">Lorem ipsum dolor sit amet consectetur. Sem sit pellentesque mauris proin tortor pellentesque.</p>
      <div class="btn-report">Report</div>
      <div class="setup">
        <div class="progress">05</div>
        <h3>Please complete basic Setup</h3>
        <ul class="steps"><li class="link">Service Charge Schedules</li><li>Service Charge Appointment</li><li>Invite residents &amp; leaseholders</li><li>Connect payment provider</li></ul>
        <svg class="icon chev"><use href="#i-down"/></svg>
      </div>
      <div class="tabs"><div class="tab on">Summary</div><div class="tab">Details</div></div>
      <div class="card general">
        <div class="card-head"><h4>General</h4><span class="view">View Detail <svg class="icon"><use href="#i-chev"/></svg></span></div>
        <dl class="rows">
          <div class="row"><dt>Units</dt><dd>85</dd></div>
          <div class="row"><dt>Address</dt><dd>42 Larchmere Road, London, N4 2QT</dd></div>
          <div class="row"><dt>Section 20 Limites</dt><dd>12</dd></div>
          <div class="row"><dt>Handover Date</dt><dd>NA</dd></div>
        </dl>
      </div>
      <div class="card-grid">
        <div class="card">
          <div class="card-head"><h4>Compliance</h4><span class="view">View Detail <svg class="icon"><use href="#i-chev"/></svg></span></div>
          <dl class="rows">
            <div class="row"><dt>Asbestos <svg class="icon info"><use href="#i-info"/></svg></dt><dd>NA</dd></div>
            <div class="row"><dt>Legionellas <svg class="icon info alert"><use href="#i-help"/></svg></dt><dd>--</dd></div>
            <div class="row"><dt>Gutter</dt><dd>Overdue 10/12/2023</dd></div>
            <div class="row"><dt>Gutters</dt><dd>NA</dd></div>
            <div class="row"><dt>Dry Risers</dt><dd>NA</dd></div>
          </dl>
        </div>
        <div class="card">
          <div class="card-head"><h4>Insurance</h4><span class="view">View Detail <svg class="icon"><use href="#i-chev"/></svg></span></div>
          <dl class="rows">
            <div class="row"><dt>Terrorism</dt><dd>NA</dd></div>
            <div class="row"><dt>Buildings</dt><dd>NA</dd></div>
            <div class="row"><dt>Engineering</dt><dd>NA</dd></div>
            <div class="row"><dt>D&amp;O</dt><dd>NA</dd></div>
            <div class="row"><dt>Reinstatement</dt><dd>NA</dd></div>
          </dl>
        </div>
        <div class="card">
          <div class="card-head"><h4>Service Charge</h4><span class="view">View Detail <svg class="icon"><use href="#i-chev"/></svg></span></div>
          <dl class="rows">
            <div class="row"><dt>Year End</dt><dd>12/12/2024</dd></div>
            <div class="row"><dt>Demand Dates</dt><dd>NA</dd></div>
          </dl>
        </div>
        <div class="card">
          <div class="card-head"><h4>Cases</h4><span class="view">View Detail <svg class="icon"><use href="#i-chev"/></svg></span></div>
          <dl class="rows">
            <div class="row"><dt>Are we Responsible ? <svg class="icon info"><use href="#i-info"/></svg></dt><dd>No</dd></div>
            <div class="row"><dt>Demand Dates</dt><dd>NA</dd></div>
          </dl>
        </div>
      </div>
    </main>
    <div class="dropdown">
      <div><svg class="icon"><use href="#i-user"/></svg>Edit Profile</div>
      <div><svg class="icon"><use href="#i-help"/></svg>Help</div>
      <div class="logout"><svg class="icon"><use href="#i-logout"/></svg>Logout</div>
    </div>
  </section>

  <!-- ===== Page 2 ===== -->
  <div class="section-band" style="left:93px;top:723px;width:941px">Page 2</div>
  <section class="app" style="left:93px;top:774px">
    <header class="topbar">
      <svg class="icon menu"><use href="#i-menu"/></svg>
      <div class="brand">Larkhill</div>
      <div class="search"><svg class="icon"><use href="#i-search"/></svg>Search</div>
      <div class="bell"><svg class="icon"><use href="#i-bell"/></svg><span class="dot">4</span></div>
      <div class="avatar" role="img" aria-label="Profile photo of the signed-in user"></div>
      <div class="user"><b>Dan Fallow</b><span>Account</span></div>
      <div class="user-caret"></div>
    </header>
    <nav class="sidebar">
      <div class="nav-item active"><svg class="icon"><use href="#i-user"/></svg><span>User Directory</span></div>
      <div class="nav-item"><svg class="icon"><use href="#i-swap"/></svg><span>Switch Development</span></div>
      <div class="nav-item"><svg class="icon"><use href="#i-dollar"/></svg><span>Service Change</span></div>
      <div class="nav-item"><svg class="icon"><use href="#i-doc"/></svg><span>Property Balane</span></div>
      <div class="nav-item"><svg class="icon"><use href="#i-mail"/></svg><span>Sending Letter</span></div>
      <div class="nav-item"><svg class="icon"><use href="#i-file"/></svg><span>Regular Services</span></div>
    </nav>
    <main class="main">
      <h1 class="page-title" style="left:26px"><svg class="icon"><use href="#i-back"/></svg>Finances</h1>
      <p class="page-sub" style="left:49px">Lorem ipsum dolor sit amet consectetur. Sem sit pellentesque mauris proin tortor pellentesque.</p>
      <div class="row-card" style="top:66px">Subaccount<svg class="icon"><use href="#i-chev"/></svg></div>
      <div class="row-card" style="top:116px;height:40px"><span class="label">Payment Provider<span class="badge">Connected</span></span><svg class="icon"><use href="#i-chev"/></svg></div>
    </main>
  </section>

  <!-- ===== Mobile app ===== -->
  <div class="section-band" style="left:1127px;top:723px;width:941px">Mobile app</div>

  <!-- Overview screen -->
  <section class="phone" style="left:1127px;top:774px;height:793px">
    <div class="status">09:09<span class="bars"><i style="width:9px;height:5px"></i><i style="width:6px;height:5px;border-radius:50%"></i><i style="width:13px;height:6px"></i></span></div>
    <div class="phone-head"><svg class="icon"><use href="#i-menu"/></svg><span class="greet">Hi, Dan Fallow</span><svg class="icon alarm"><use href="#i-bell"/></svg></div>
    <div class="body" style="top:53px">
      <h2 class="over-title">Overview</h2>
      <p class="over-sub">Lorem ipsum dolor sit amet consectetur. Sem sit pellentesque mauris proin tortor pellentesque.</p>
    </div>
    <div class="setup body" style="top:102px">
      <div class="progress" style="top:5px">05</div>
      <h3>Please complete basic Setup</h3>
      <div class="toggle" style="top:14px"></div>
    </div>
    <div class="tabs" style="top:150px"><div class="tab on">Summary</div><div class="tab">Details</div></div>
    <div class="card body" style="top:191px;height:116px">
      <div class="card-head"><h4>General</h4><span class="view">View Detail <svg class="icon"><use href="#i-chev"/></svg></span></div>
      <dl class="rows">
        <div class="row"><dt>Units</dt><dd>85</dd></div>
        <div class="row" style="height:28px;align-items:flex-start;padding-top:4px"><dt>Address</dt><dd style="text-align:right;line-height:10px">42 Larchmere Road,<br>London, N4 2QT</dd></div>
        <div class="row"><dt>Section 20 Limites</dt><dd>12</dd></div>
        <div class="row"><dt>Handover Date</dt><dd>NA</dd></div>
      </dl>
    </div>
    <div class="card body" style="top:322px;height:124px">
      <div class="card-head"><h4>Compliance</h4><span class="view">View Detail <svg class="icon"><use href="#i-chev"/></svg></span></div>
      <dl class="rows">
        <div class="row"><dt>Asbestos <svg class="icon info"><use href="#i-info"/></svg></dt><dd>NA</dd></div>
        <div class="row"><dt>Legionellas <svg class="icon info alert"><use href="#i-help"/></svg></dt><dd>--</dd></div>
        <div class="row"><dt>Gutter</dt><dd>Overdue 10/12/2023</dd></div>
        <div class="row"><dt>Gutters</dt><dd>NA</dd></div>
        <div class="row"><dt>Dry Risers</dt><dd>NA</dd></div>
      </dl>
    </div>
    <div class="card body" style="top:461px;height:124px">
      <div class="card-head"><h4>Insurance</h4><span class="view">View Detail <svg class="icon"><use href="#i-chev"/></svg></span></div>
      <dl class="rows">
        <div class="row"><dt>Terrorism</dt><dd>NA</dd></div>
        <div class="row"><dt>Buildings</dt><dd>NA</dd></div>
        <div class="row"><dt>Engineering</dt><dd>NA</dd></div>
        <div class="row"><dt>D&amp;O</dt><dd>NA</dd></div>
        <div class="row"><dt>Reinstatement</dt><dd>NA</dd></div>
      </dl>
    </div>
    <div class="card body" style="top:599px;height:71px">
      <div class="card-head"><h4>Service Charge</h4><span class="view">View Detail <svg class="icon"><use href="#i-chev"/></svg></span></div>
      <dl class="rows">
        <div class="row"><dt>Year End</dt><dd>12/12/2024</dd></div>
        <div class="row"><dt>Demand Dates</dt><dd>NA</dd></div>
      </dl>
    </div>
    <div class="card body" style="top:683px;height:54px">
      <div class="card-head"><h4>Coses</h4><span class="view">View Detail <svg class="icon"><use href="#i-chev"/></svg></span></div>
      <dl class="rows">
        <div class="row"><dt>Are we Responsible ? <svg class="icon info"><use href="#i-info"/></svg></dt><dd>No</dd></div>
      </dl>
    </div>
    <nav class="bottom-nav" style="top:740px">
      <div class="nav-tab on"><svg class="icon"><use href="#i-home"/></svg>Home</div>
      <div class="nav-tab"><svg class="icon"><use href="#i-doc"/></svg>Overview</div>
      <div class="nav-tab"><svg class="icon"><use href="#i-dollar"/></svg>Finances</div>
      <div class="nav-tab"><svg class="icon"><use href="#i-msg"/></svg>Message</div>
    </nav>
    <div class="home-bar" style="top:786px"></div>
  </section>

  <!-- Finance screen -->
  <section class="phone" style="left:1361px;top:774px;height:456px">
    <div class="status" style="padding-top:3px">09:09<span class="bars" style="top:5px"><i style="width:9px;height:4px"></i><i style="width:6px;height:4px;border-radius:50%"></i><i style="width:12px;height:4px"></i></span></div>
    <div class="phone-head" style="top:20px;height:28px"><svg class="icon"><use href="#i-back"/></svg>Finance</div>
    <div class="card body" style="top:54px;height:152px">
      <div class="card-head" style="border-bottom:0;height:27px"><h4>Accounts Receivable</h4></div>
      <div class="sub-divider" style="margin-top:0"></div>
      <dl class="rows">
        <div class="row"><dt>Arrears</dt><span class="view">View Detail <svg class="icon"><use href="#i-chev"/></svg></span></div>
        <div class="row"><dt style="font-weight:400">Total</dt><dd>$23,000</dd></div>
        <div class="row"><dt style="font-weight:400">Bills</dt><dd>5</dd></div>
      </dl>
      <div class="sub-divider" style="margin-top:2px"></div>
      <dl class="rows">
        <div class="row"><dt>Unallocated Receipts</dt><span class="view">View Detail <svg class="icon"><use href="#i-chev"/></svg></span></div>
        <div class="row"><dt style="font-weight:400">Total</dt><dd>$23,000</dd></div>
        <div class="row"><dt style="font-weight:400">Receipts</dt><dd>5</dd></div>
      </dl>
    </div>
    <div class="card body" style="top:219px;height:89px">
      <div class="card-head" style="border-bottom:0;height:27px"><h4>Accounts Payable</h4></div>
      <div class="sub-divider" style="margin-top:0"></div>
      <dl class="rows">
        <div class="row"><dt>Invoices</dt><span class="view">View Detail <svg class="icon"><use href="#i-chev"/></svg></span></div>
        <div class="row"><dt style="font-weight:400">Total</dt><dd>$23,000</dd></div>
        <div class="row"><dt style="font-weight:400">Bills</dt><dd>5</dd></div>
      </dl>
    </div>
    <nav class="bottom-nav" style="top:404px;border-top:1px solid #eceef2">
      <div class="nav-tab on"><svg class="icon"><use href="#i-home"/></svg>Home</div>
      <div class="nav-tab"><svg class="icon"><use href="#i-doc"/></svg>Overview</div>
      <div class="nav-tab"><svg class="icon"><use href="#i-dollar"/></svg>Finances</div>
      <div class="nav-tab"><svg class="icon"><use href="#i-msg"/></svg>Message</div>
    </nav>
    <div class="home-bar" style="top:450px"></div>
  </section>

  <!-- Legionellas screen -->
  <section class="phone" style="left:1594px;top:774px;height:456px">
    <div class="status" style="padding-top:3px">09:09<span class="bars" style="top:5px"><i style="width:9px;height:4px"></i><i style="width:6px;height:4px;border-radius:50%"></i><i style="width:12px;height:4px"></i></span></div>
    <div class="phone-head" style="top:20px;height:28px"><svg class="icon"><use href="#i-back"/></svg>Legionellas</div>
    <div class="body" style="top:54px">
      <p class="question">Is it required ?</p>
    </div>
    <div class="body" style="top:75px">
      <div class="option"><span class="radio on"></span>No</div>
      <div class="option"><span class="radio"></span>Yes, but i do not have a file to upload</div>
      <div class="option"><span class="radio"></span>Yes, and i have a file to upload</div>
    </div>
    <div class="actions" style="top:406px">
      <div class="btn-ghost">Back</div>
      <div class="btn-solid">Nest</div>
    </div>
    <div class="home-bar" style="top:450px"></div>
  </section>
</div>
</body>
</html>
```